Childrens Business Card Design Project

We have an existing logo attached which we'd like to use as part of our new business card design.

The design needs to be relatively gender neutral and contain bright colours.

In terms of look and feel think:

Fun, Modern, Quality (as opposed to cheap!) and of course Party!

Single or double sided - i am not decided on either one yet - ideally i'd like to see designs for both because if you think stylistically it would benefit having two sides then please try it out!

I think the challenge here is finding a really good background colour (if you think it needs one) and also choosing an eye grabbing text that compliments the existing logo - do that an you are onto a winner! I have another image for the business (which i have attached) which uses stripes so i am keen to see a design that incorporates this to tie in all my collateral.

The copy required is as follows (not necesarily in this order)

Bookings/Enquiries:

Tilda

T: 0498 765 210
E: enquiries@brixtopia.com.au

ABN: 43 527 806 214

Any feedback on text is welcomed - please message me or add to the discussion.

Reason: Hi All, I have received some promising designs, but overall i am not impressed with the quality of the work so have extended the deadline as this project has been committed. I will aim to attach some business card examples to the brief tomorrow to give further guidance as a whole but please do not submit any designs on a generic background that are not related to the theme, have been carelessly placed with overlapping elements - it just looks sloppy. For those who have read the brief an incorporated stripes or even spots this is on target as it convey's a party theme, however please work on getting the colours for the contact details by either a bold solid strip to highlight or some other way to frame it. When it comes to the logo, some people have removed the characters all together and changed the colour of the wording - this is fine. Also feel free to balloons starts - but keep it classy and watch your placement of these. I hope this helps and for the designs i would like to see revisions for i will aim to get back to you individually over the next day or so. Many thanks all.

Target Market(s)

Mothers in the suburbs of Australia with a disposal able income, children aged between 1-7 years old.

Industry/Entity Type

Business

Requirements
Must have
• The font and wording positioning must compliment the logo.

```html
<!DOCTYPE html>
<html lang="en">
<head>
<meta charset="utf-8">
<title>Brixtopia – Business Card</title>
<link rel="stylesheet" href="https://fonts.googleapis.com/css2?family=Ubuntu:wght@400;500&display=swap">
<style>
  :root {
    --page: #ecebf2;
    --lavender: #8282c2;
    --lavender-dark: #6c6cb0;
    --white: #ffffff;
    --butter: #f6e98e;
    --butter-deep: #efd96a;
    --ink-blue: #1f7fc6;
    --tag-orange: #e8842c;
    --ink-dark: #4a4a7a;
    --art-warm: #f2c6a8;
    --art-cool: #b9d8ec;
  }
  * { box-sizing: border-box; margin: 0; padding: 0; }
  html, body {
    width: 1200px; height: 899px; overflow: hidden;
    background: var(--page);
    font-family: "Ubuntu", sans-serif;
  }
  .stage {
    position: relative; width: 1200px; height: 899px;
    display: flex; flex-direction: column; align-items: center; justify-content: center; gap: 44px;
  }
  .card {
    position: relative; width: 600px; height: 366px;
    background: var(--white); overflow: hidden;
    box-shadow: 0 6px 18px rgba(60, 60, 100, 0.18);
  }

  /* ---------- contact side ---------- */
  .card-contact .brand {
    position: absolute; left: 200px; top: 28px; width: 300px; height: 120px;
  }
  .brand-art {
    position: absolute; left: 10px; top: 0; width: 280px; height: 64px;
    border-radius: 10px;
    background: linear-gradient(90deg, var(--art-warm), #f6dc8c 50%, var(--art-cool));
  }
  .brand-name {
    position: absolute; left: 0; right: 0; top: 62px; text-align: center;
    font-size: 40px; font-weight: 500; letter-spacing: 3px; color: var(--ink-blue);
  }
  .brand-tag {
    position: absolute; left: 0; right: 0; top: 108px; text-align: center;
    font-size: 9px; color: var(--tag-orange); letter-spacing: .5px;
  }
  .info-band {
    position: absolute; left: 0; right: 0; top: 168px; bottom: 0;
    background: var(--lavender);
  }
  .info-band::before {
    content: ""; position: absolute; left: 0; right: 0; top: -10px; height: 10px;
    background: radial-gradient(circle at 9px 10px, var(--lavender) 9px, transparent 9.5px) repeat-x;
    background-size: 18px 10px;
  }
  .info { position: absolute; color: var(--butter); font-size: 17px; }
  .badge {
    display: inline-flex; align-items: center; justify-content: center;
    width: 28px; height: 28px; border-radius: 50%;
    background: var(--butter); color: var(--ink-dark);
    font-size: 14px; margin-right: 6px; vertical-align: middle;
  }
  .info-phone { left: 40px; top: 36px; }
  .info-bookings {
    left: 250px; width: 260px; top: 32px; text-align: center;
    font-weight: 500; font-size: 17px; line-height: 1.15;
  }
  .info-email { left: 300px; top: 96px; }
  .info-abn { left: 240px; top: 150px; font-size: 13px; }

  /* ---------- striped side ---------- */
  .card-stripes {
    background: repeating-linear-gradient(90deg,
      var(--white) 0 14px, var(--lavender) 14px 38px, var(--white) 38px 52px);
  }
  .band {
    position: absolute; left: 0; right: 0; top: 108px; height: 150px;
    background: var(--white);
    border-top: 5px solid var(--butter); border-bottom: 5px solid var(--butter);
    box-shadow: inset 0 2px 0 var(--lavender-dark), inset 0 -2px 0 var(--lavender-dark);
  }
  .oval {
    position: absolute; left: 132px; top: 76px; width: 336px; height: 214px;
    border-radius: 50%; background: var(--butter);
    display: flex; align-items: center; justify-content: center;
  }
  .oval-inner {
    position: relative; width: 310px; height: 190px; border-radius: 50%;
    background: var(--white); border: 2px solid var(--lavender-dark);
  }
  .oval-inner .brand-art {
    left: 30px; top: 22px; width: 246px; height: 62px;
  }
  .oval-inner .brand-name { top: 84px; font-size: 38px; }
  .oval-inner .brand-tag { top: 130px; }
</style>
</head>
<body>
<main class="stage">

  <section class="card card-contact" aria-label="Contact side">
    <div class="brand">
      <div class="brand-art" role="img" aria-label="Cartoon party characters: a fairy, a clown doing a handstand and a pirate"></div>
      <div class="brand-name">Brixtopia</div>
      <div class="brand-tag">Kids Parties &amp; Events</div>
    </div>
    <div class="info-band">
      <p class="info info-phone"><span class="badge">T:</span>0498 765 210</p>
      <p class="info info-bookings">Bookings/Enquiries:<br>Tilda</p>
      <p class="info info-email"><span class="badge">E:</span>enquiries@brixtopia.com.au</p>
      <p class="info info-abn">ABN: 43 527 806 214</p>
    </div>
  </section>

  <section class="card card-stripes" aria-label="Logo side">
    <div class="band"></div>
    <div class="oval">
      <div class="oval-inner">
        <div class="brand-art" role="img" aria-label="Cartoon party characters: a fairy, a clown doing a handstand and a pirate"></div>
        <div class="brand-name">Brixtopia</div>
        <div class="brand-tag">Kids Parties &amp; Events</div>
      </div>
    </div>
  </section>

</main>
</body>
</html>
```